Daybreak Ledger Booklet

I have a 25 page booklet that I wrote.
I need to have a book cover design, typesetting, and imagery.
I need it to be designed with bleeds because I am having it printed.
It will be in an 8.5 X 11 format.
Please look at the 2020*.png files for an idea for the cover.
The title of the mini-book is "Daybreak Ledger" .
Subtitle is "Crestlo Method for Health and Fitness Motivation"
Then in between the title and subtitle, place the "Tobin_Health_Infographic...." image.
The other images are for inside the mini-book,
The "Daybreak-Ledger-CrestlO.pdf" file is the information in the book that will need to be typesetted.
The other images are inside the book and will need to be placed inside when appropriate.
Please don't agree to do this project if you have not done this before
I also want to see your portfolio.
Thank you
P.S. I can add all my images that are in the booklet when you accept project

Target Market(s)

Baby boomers ages 50-70

Industry/Entity Type

Fitness

Colors
0a5aa6

Requirements
Must have
• My project consists of a book cover and back. And typesetting and imagery inside the book.

```html
<!DOCTYPE html>
<html lang="en">
<head>
<meta charset="utf-8">
<title>Daybreak Ledger – Spread 2–3</title>
<link href="https://fonts.googleapis.com/css2?family=Arimo:wght@400;700&display=swap" rel="stylesheet">
<style>
  :root {
    --brand-blue: #0a5aa6;
    --ink: #111111;
    --paper: #ffffff;
    --photo-top: #b9b2c4;
    --photo-bottom: #6f6a78;
  }
  * { box-sizing: border-box; margin: 0; padding: 0; }
  html, body { width: 1200px; height: 786px; overflow: hidden; background: var(--paper); }
  body { font-family: "Arimo", Arial, sans-serif; color: var(--ink); position: relative; }

  .spread { position: absolute; inset: 0; width: 1200px; height: 786px; }
  .page { position: absolute; top: 0; width: 600px; height: 786px; }
  .page--left { left: 0; }
  .page--right { left: 600px; }

  .wordmark {
    position: absolute; top: 40px;
    font-weight: 700; font-size: 26px; letter-spacing: 0.5px;
    color: var(--brand-blue); text-transform: uppercase;
  }
  .page--left .wordmark { left: 262px; }
  .page--right .wordmark { left: 248px; }

  .section-title {
    position: absolute; top: 124px; height: 26px;
    display: flex; align-items: center; gap: 8px;
    color: var(--brand-blue); font-weight: 700; font-size: 19.5px; letter-spacing: 0.2px;
  }
  .section-title .rule { flex: 1; height: 4px; background: var(--brand-blue); }
  .page--left .section-title { left: 137px; width: 346px; }
  .page--right .section-title { left: 78px; width: 448px; }

  .copy { position: absolute; font-size: 12.6px; line-height: 16.3px; }
  .copy p { margin-bottom: 8.6px; }
  .copy .lead { font-weight: 700; }
  .copy .indent { margin-left: 55px; }
  .page--left .copy { left: 137px; top: 163px; width: 350px; }
  .page--left .copy .lead.second { margin-top: 16px; }
  .page--right .copy { left: 78px; top: 155px; width: 450px; }
  .copy .narrow { width: 275px; }
  .copy .callout { color: var(--brand-blue); font-weight: 700; }

  .photo {
    position: absolute; left: 365px; top: 432px; width: 152px; height: 191px;
    background: linear-gradient(160deg, var(--photo-top), var(--photo-bottom));
    border: 1px solid #555; box-shadow: 4px 4px 5px rgba(0,0,0,0.45);
  }

  .footer-band { position: absolute; left: 0; top: 688px; width: 1200px; height: 98px; }
  .footer-note {
    position: absolute; top: 743px; font-size: 9.5px; color: var(--paper);
  }
  .page--left .footer-note { left: 177px; }
  .page--right .footer-note { left: 111px; }
  .folio {
    position: absolute; top: 725px; width: 40px; text-align: center;
    color: #cfe0f2; font-size: 17px;
  }
  .page--left .folio { left: 31px; }
  .page--right .folio { left: 529px; }
</style>
</head>
<body>
<div class="spread">
  <svg class="footer-band" viewBox="0 0 1200 98" aria-hidden="true">
    <polygon fill="var(--brand-blue)" points="0,0 84,0 120,37 1078,37 1113,0 1200,0 1200,98 0,98"/>
    <g fill="none" stroke="#cfe0f2" stroke-width="1.2">
      <polyline points="41,25 32,25 32,68 41,68"/>
      <polyline points="62,25 71,25 71,68 62,68"/>
      <polyline points="1139,25 1130,25 1130,68 1139,68"/>
      <polyline points="1160,25 1169,25 1169,68 1160,68"/>
    </g>
  </svg>

  <section class="page page--left">
    <div class="wordmark">Crestlo</div>
    <h2 class="section-title"><span class="rule"></span>FORWARD<span class="rule"></span></h2>
    <div class="copy">
      <p class="lead">This manifesto could change your life.</p>
      <p class="indent">I know it seems rather bold to claim that you can sit down for the next few minutes and read something that could alter the course of your life. In fact, I wouldn’t have believed it myself just a few short years ago.</p>
      <p class="indent">But three years ago, at the age of sixty-three, I started on a journey that would change my life forever. What you are reading right now is the result of three years of experimentation, reading, watching, testing, and taking ACTION that has allowed me to achieve a high degree of fitness and health <strong>in my sixties.</strong></p>
      <p class="indent">This manifesto is going to upset the “apple cart” big time. A lot of fitness trainers, local gyms, and companies in the health and fitness industry are going to be very pissed at me.</p>
      <p class="lead second">But what I’ve learned is too powerful to keep to myself, so I just had to share it with you.</p>
      <p class="indent">Before we get started, spend a few moments studying the cover page of this document. It may feel a little overwhelming, but I promise you’ll understand it when you finish this manifesto.</p>
      <p class="indent">As you read, my hope is that you will begin to see the “Big Takeaway”. This takeaway has changed my life. And my hope and dream is that it does the same for you.</p>
    </div>
    <div class="folio">2</div>
    <div class="footer-note">© 2019 Brightfield Press LLC · Web https://www.crestlo.com</div>
  </section>

  <section class="page page--right">
    <div class="wordmark">Crestlo</div>
    <h2 class="section-title"><span class="rule"></span>WHO IS TOBIN HALE<span class="rule"></span></h2>
    <div class="copy">
      <p>First of all, I’m not the famous actor.</p>
      <p>If you did a Seekly search on “Tobin Hale,” you’d get two or three pages of the Hollywood star.</p>
      <p>I’m certainly not a star and have no ambition to be one. My story isn’t made in Hollywood.</p>
      <p>Four years ago, after thirty-two years of marriage, my sixty-two-year-old wife suddenly died of a brain aneurysm while we were watching the College Football Championship game on TV. It was so fast and incredibly devastating. Unless you’ve experienced it, you don’t understand how quickly those we love can be gone.</p>
      <p>If it hadn’t been for my children and family, I would have gone into a much deeper depression than I did.</p>
      <p>Yet I did what many of us would do. I attempted to find relief in TV, food, and alcohol. As you may know, it’s very easy to put on weight when you are inactive and over sixty.</p>
      <p class="narrow">To this day, I don’t recall who took this picture of me. But I’m eternally grateful for the wake-up call!</p>
      <p class="narrow">I feel awkward when I start to discuss this (and I mention it only because it’s urgent that you begin to understand how powerful the methods I’m going to reveal to you are), but my transformation – starting at the age of sixty-three—is quite amazing according to friends, family, and even strangers.</p>
      <p>I’ll show you current pictures later. And I’m doing that for a reason.</p>
      <p class="callout">THIS MANIFESTO IS ABOUT YOU, NOT ME.</p>
      <p>This manifesto was written for YOU!You are the hero in this story.</p>
    </div>
    <div class="photo" role="img" aria-label="Snapshot of the author seated on a sofa at home, eating, before his fitness transformation"></div>
    <div class="folio">3</div>
    <div class="footer-note">© 2019 Brightfield Press LLC · Web https://www.crestlo.com</div>
  </section>
</div>
</body>
</html>
```